Tervolan Pty Ltd professional business card

A professional business card template using the colours from the supplied logo.
Clean crisp lines while, Modern while not being over the top.

Target Market(s)

Construction, commerical and industrial

Industry/Entity Type

Communications

Contact Information for Business Card

For a Communications, IT, Optical fibre installation company

Colors
37b8a4

```html
<!DOCTYPE html>
<html lang="en">
<head>
<meta charset="utf-8">
<title>Tervolan Pty Ltd — Business Card</title>
<link href="https://fonts.googleapis.com/css2?family=Montserrat:wght@400;500;600&display=swap" rel="stylesheet">
<style>
  :root {
    --page-bg: #e4e5e7;
    --card-dark: #0d0e10;
    --card-teal: #0b8a9c;
    --accent: #1aa6b8;
    --accent-bright: #22e3f0;
    --text-grey: #8a8c90;
    --logo-grey: #8d8f93;
    --rule: #4a4c50;
  }
  * { margin: 0; padding: 0; box-sizing: border-box; }
  html, body { width: 1200px; height: 800px; overflow: hidden; }
  body {
    background: var(--page-bg);
    font-family: "Montserrat", sans-serif;
    display: flex;
    align-items: center;
    justify-content: center;
    gap: 40px;
  }
  .card {
    width: 540px;
    height: 310px;
    border-radius: 18px;
    position: relative;
    box-shadow: 0 12px 30px rgba(0,0,0,0.22);
  }
  .card--front { background: var(--card-dark); }
  .card--back {
    background: linear-gradient(135deg, #0f9aab 0%, var(--card-teal) 60%, #077a8b 100%);
    display: flex; align-items: center; justify-content: center;
  }
  .brand {
    position: absolute; left: 48px; top: 78px;
    display: flex; align-items: center; gap: 12px;
  }
  .brand__mark { width: 22px; height: 22px; background: var(--accent); }
  .brand__name {
    font-weight: 500; font-size: 40px; letter-spacing: 2px;
    color: var(--logo-grey);
  }
  .person { position: absolute; left: 48px; top: 168px; }
  .person__name {
    font-weight: 600; font-size: 17px; letter-spacing: 0.5px;
    color: var(--accent); text-transform: uppercase;
  }
  .person__title { font-size: 13px; color: var(--text-grey); margin-top: 3px; }
  .person__address { font-size: 12px; color: var(--text-grey); margin-top: 16px; line-height: 1.6; }
  .divider {
    position: absolute; left: 318px; top: 110px;
    width: 1px; height: 110px; background: var(--rule);
  }
  .contact { position: absolute; left: 340px; top: 112px; list-style: none; }
  .contact li {
    display: flex; align-items: center; gap: 10px;
    font-size: 12.5px; color: var(--text-grey); height: 26px;
  }
  .contact svg { width: 12px; height: 12px; fill: var(--accent); flex: none; }
  .back-name {
    font-weight: 500; font-size: 60px; letter-spacing: 3px;
    color: var(--accent-bright);
    display: flex; align-items: center; gap: 16px;
  }
  .back-name__mark { width: 30px; height: 30px; background: var(--accent-bright); }
</style>
</head>
<body>
  <section class="card card--front">
    <div class="brand">
      <span class="brand__mark"></span>
      <span class="brand__name">TERVOLAN</span>
    </div>
    <div class="person">
      <p class="person__name">Daniel Harrow</p>
      <p class="person__title">President</p>
      <p class="person__address">4120 Ridgeline Road<br>Northvale, Ontario 58213</p>
    </div>
    <div class="divider"></div>
    <ul class="contact">
      <li><svg viewBox="0 0 12 12"><path d="M2.5 0.5 4.5 3 3.5 4.5c.7 1.6 2 2.9 3.6 3.6L8.6 7 11.5 9 10.5 11.3C5 11 1 7 .7 1.5Z"/></svg>555-204-7731</li>
      <li><svg viewBox="0 0 12 12"><path d="M3 0h6a1 1 0 0 1 1 1v10a1 1 0 0 1-1 1H3a1 1 0 0 1-1-1V1a1 1 0 0 1 1-1Zm0 1.5V9.5h6V1.5Z"/></svg>555-318-6642</li>
      <li><svg viewBox="0 0 12 12"><path d="M0 2h12v8H0Zm1 1v.4l5 3.3 5-3.3V3Zm0 1.6V9h10V4.6L6 7.9Z"/></svg>info@tervolan.com</li>
      <li><svg viewBox="0 0 12 12"><path d="M6 0a6 6 0 1 0 0 12A6 6 0 0 0 6 0Zm0 1.2a4.8 4.8 0 0 1 4.4 3H7.8a8 8 0 0 0-1-2.8Zm-2 .3a8 8 0 0 0-1 2.7H1.6A4.8 4.8 0 0 1 4 1.5ZM1.3 5.4h1.6a9 9 0 0 0 0 1.2H1.3Zm9.4 0a4.8 4.8 0 0 1 0 1.2H9.1a9 9 0 0 0 0-1.2ZM1.6 7.8H3a8 8 0 0 0 1 2.7 4.8 4.8 0 0 1-2.4-2.7Zm6.2 0h2.6a4.8 4.8 0 0 1-3.6 3 8 8 0 0 0 1-3Z"/></svg>www.tervolan.com</li>
    </ul>
  </section>
  <section class="card card--back">
    <div class="back-name">
      <span class="back-name__mark"></span>
      <span>TERVOLAN</span>
    </div>
  </section>
</body>
</html>
```